Simple Business Card Design for Foodie

Job:

Make a very simple, minimalist business card design with my details including adjusted logo. One side to be white (with logo & text). Other side to be yellow - try plain or with logo (or part of logo eg Z). Need business card to have continuity with website.

Logo:
Our logo is made from a free download font website:
http://www.glyphbarn.net/search.php?q=rubber
but the spacing/kerning needs correcting/adjusting as the font spaces unevenly between letters (see attached files). Need logo to be very crisp/sharp when printed.

Printing:
We will be using Parcly.com so the design needs to conform to their requirements, see here:

http://uk.parcly.com/products/velin/business-cards.html (scroll down for dimensions and guidelines)

Design:

must say "plant-based food consulting" underneath logo or somewhere
no address needed in contact section
sharp corners (not rounded)
one side white, one side yellow

name: Marisol Quenby
1xmobile number: +44 7700 900431
1xtwiiter: @quillcounsel
website address www.greenplatehub.example
email address quill@greenplatehub.example

Should be easy quick job, prompt + detailed feedback given, am online in UK 9am-10pm for next 3 days. Website is www.greenplatehub.example

Must have
• The logo must be corrected. The kerning is not right.

Please use a warm-grey for text

Please submit in matt format, we will be printing matt finish.

Should not have
• Avoid using banners or curvy highlights

Please avoid using black

Please avoid submitting in gloss finish

```html
<!DOCTYPE html>
<html lang="en">
<head>
<meta charset="utf-8">
<title>Quill – Business Card</title>
<link rel="stylesheet" href="https://fonts.googleapis.com/css2?family=Arimo:wght@400;700&display=swap">
<style>
  :root {
    --backdrop: #4b4b4b;
    --card-white: #f3f3f2;
    --card-yellow: #f4dc2e;
    --brand-amber: #e8a90c;
    --warm-grey: #4d4945;
    --warm-grey-soft: #5e5955;
    --rule: #d9d7d4;
  }
  * { margin: 0; padding: 0; box-sizing: border-box; }
  html, body {
    width: 1200px;
    height: 1000px;
    overflow: hidden;
    background: var(--backdrop);
    font-family: "Arimo", Arial, sans-serif;
  }
  .stage { position: relative; width: 1200px; height: 1000px; }

  .card {
    position: absolute;
    width: 532px;
    height: 303px;
  }
  .card--front { left: 231px; top: 175px; background: var(--card-white); }
  .card--back  { left: 397px; top: 522px; background: var(--card-yellow); }

  .brand {
    position: absolute;
    left: 51px;
    top: 88px;
    font-weight: 700;
    font-size: 58px;
    line-height: 1;
    letter-spacing: 4px;
    color: var(--brand-amber);
  }
  .tagline {
    position: absolute;
    right: 336px;
    top: 189px;
    text-align: right;
    font-size: 12.5px;
    line-height: 15px;
    color: var(--warm-grey-soft);
    text-transform: uppercase;
  }
  .divider {
    position: absolute;
    left: 251px;
    top: 57px;
    width: 1px;
    height: 193px;
    background: var(--rule);
  }
  .details {
    position: absolute;
    left: 298px;
    top: 93px;
    color: var(--warm-grey);
  }
  .details__name {
    font-weight: 700;
    font-size: 17px;
    letter-spacing: 0.6px;
    text-transform: uppercase;
    line-height: 20px;
  }
  .details__role {
    font-size: 13px;
    line-height: 16px;
    color: var(--warm-grey-soft);
  }
  .contact-list {
    list-style: none;
    margin-top: 20px;
  }
  .contact-list li {
    display: flex;
    align-items: center;
    gap: 6px;
    font-size: 13px;
    line-height: 18px;
    color: var(--warm-grey-soft);
  }
  .contact-list svg { width: 12px; height: 12px; flex: none; }
</style>
</head>
<body>
<main class="stage">
  <section class="card card--front" aria-label="Business card, front">
    <div class="brand">QUILL</div>
    <p class="tagline">Plant-based<br>food consulting</p>
    <div class="divider"></div>
    <div class="details">
      <h1 class="details__name">Marisol Quenby</h1>
      <p class="details__role">General Manager</p>
      <ul class="contact-list">
        <li>
          <svg viewBox="0 0 12 12" aria-hidden="true"><circle cx="6" cy="6" r="5.3" fill="none" stroke="#e8a90c" stroke-width="1.1"/><path d="M4 3.3l1 1-.6.8a4 4 0 0 0 2.5 2.5l.8-.6 1 1-.7.8C5.8 8.6 3.4 6.2 3.2 4z" fill="#e8a90c"/></svg>
          +44 7700 900431
        </li>
        <li>
          <svg viewBox="0 0 12 12" aria-hidden="true"><circle cx="6" cy="6" r="5.3" fill="none" stroke="#e8a90c" stroke-width="1.1"/></svg>
          @quillcounsel
        </li>
        <li>
          <svg viewBox="0 0 12 12" aria-hidden="true"><circle cx="6" cy="6" r="5.3" fill="none" stroke="#e8a90c" stroke-width="1.1"/><rect x="3.2" y="4.2" width="5.6" height="3.8" fill="none" stroke="#e8a90c" stroke-width="0.9"/><path d="M3.2 4.2L6 6.4l2.8-2.2" fill="none" stroke="#e8a90c" stroke-width="0.9"/></svg>
          quill@greenplatehub.example
        </li>
        <li>
          <svg viewBox="0 0 12 12" aria-hidden="true"><circle cx="6" cy="6" r="5.3" fill="none" stroke="#e8a90c" stroke-width="1.1"/><ellipse cx="6" cy="6" rx="2.2" ry="5.3" fill="none" stroke="#e8a90c" stroke-width="0.8"/><path d="M0.7 6h10.6M1.5 3.5h9M1.5 8.5h9" stroke="#e8a90c" stroke-width="0.8"/></svg>
          www.greenplatehub.example
        </li>
      </ul>
    </div>
  </section>

  <section class="card card--back" aria-label="Business card, back"></section>
</main>
</body>
</html>
```